Flyer Design

I need a nice professional flyer design to use for advertising my lawn/snow removal business. Flyers I am using are 5.47"x4.21". I've attached a flyer I found online that I liked. Just wanting something creative and professional. The images of the logos I attached are of the original logo design, and the new color design we are using. There is also a mockup of our tshirt design to give you an idea of the actual color on the tshirt, since the jpeg logo isn't exactly accurate on color.
Things I need on the flyer in no particular order:
"Snow is coming"
"Don't Wait Until It's TOO LATE!"
"Free Estimates"
Services offered
"Commercial/Residential"
"Snow Plowing"
"Snow Blowing"
"Snow Shoveling"
"Ice Removal"
"Salting/Sanding"
"Fully Licensed and Insured"
"Available and ON CALL 24/7"
"Seasonal Packages Available"
"CALL NOW TO RESERVE"

```html
<!DOCTYPE html>
<html lang="en">
<head>
<meta charset="utf-8">
<title>Snow Removal Flyer</title>
<link rel="stylesheet" href="https://fonts.googleapis.com/css2?family=Cabin:wght@400;600;700&family=Oleo+Script:wght@700&family=Kaushan+Script&display=swap">
<style>
  :root {
    --orange: #f07020;
    --orange-deep: #e2621a;
    --charcoal: #3a3a3c;
    --ink: #111111;
    --white: #ffffff;
    --shadow: rgba(40, 40, 40, 0.55);
  }
  * { margin: 0; padding: 0; box-sizing: border-box; }
  html, body { width: 1200px; height: 924px; overflow: hidden; background: var(--white); }
  .flyer {
    position: relative;
    width: 1200px;
    height: 924px;
    overflow: hidden;
    font-family: "Cabin", sans-serif;
    background: var(--white);
  }
  .backdrop { position: absolute; inset: 0; }

  .estimate-badge {
    position: absolute;
    left: 336px; top: 216px;
    width: 180px; height: 180px;
    border-radius: 50%;
    background: var(--orange);
    display: flex; align-items: center; justify-content: center;
  }
  .estimate-badge__inner {
    width: 150px; height: 150px;
    border-radius: 50%;
    border: 6px solid var(--white);
    background: var(--orange);
    display: flex; flex-direction: column; align-items: center; justify-content: center;
    color: var(--white);
    font-weight: 700;
    line-height: 1.15;
    text-align: center;
  }
  .estimate-badge__free { font-size: 28px; }
  .estimate-badge__word { font-size: 26px; }

  .brand {
    position: absolute;
    right: 40px; top: 100px;
    display: flex; align-items: center; gap: 12px;
    padding: 14px 22px;
    background: var(--white);
    border-radius: 8px;
  }
  .brand__dot { width: 22px; height: 22px; border-radius: 50%; background: var(--orange); }
  .brand__name { font-size: 30px; font-weight: 700; color: var(--charcoal); letter-spacing: 0.5px; }

  .headline {
    position: absolute;
    left: 240px; top: 448px;
    width: 560px;
    text-align: center;
    font-family: "Oleo Script", cursive;
    font-weight: 700;
    font-size: 124px;
    line-height: 104px;
    color: var(--orange);
    text-shadow: 4px 5px 3px var(--shadow);
    transform: skewX(-6deg);
  }

  .urgency {
    position: absolute;
    left: 260px; top: 668px;
    width: 560px;
    text-align: center;
    font-size: 29px;
    font-weight: 700;
    color: var(--ink);
  }
  .urgency__accent { color: var(--orange); }

  .packages {
    position: absolute;
    left: 220px; top: 708px;
    width: 580px;
    text-align: center;
    font-family: "Kaushan Script", cursive;
    font-size: 40px;
    color: var(--ink);
  }

  .services { position: absolute; left: 826px; top: 482px; }
  .services__title {
    font-size: 37px;
    font-weight: 600;
    color: var(--orange);
    text-shadow: 2px 2px 2px rgba(0,0,0,0.35);
    margin-bottom: 6px;
  }
  .services__list { list-style: none; }
  .services__item {
    position: relative;
    padding-left: 30px;
    font-size: 25px;
    font-weight: 600;
    line-height: 36px;
    color: var(--ink);
  }
  .services__item::before {
    content: "";
    position: absolute;
    left: 2px; top: 12px;
    width: 13px; height: 13px;
    border-radius: 50%;
    background: var(--orange);
  }

  .credentials { position: absolute; left: 88px; top: 818px; color: var(--white); }
  .credentials__license { font-size: 24px; }
  .credentials__oncall { font-size: 35px; margin-top: 6px; }

  .reserve { position: absolute; left: 732px; top: 808px; color: var(--ink); }
  .reserve__cta { font-size: 36px; font-weight: 700; letter-spacing: -0.5px; }
  .reserve__phone { font-size: 36px; font-weight: 700; margin-top: 8px; letter-spacing: -0.5px; }
</style>
</head>
<body>
<main class="flyer">
  <svg class="backdrop" width="1200" height="924" viewBox="0 0 1200 924" aria-hidden="false">
    <defs>
      <linearGradient id="winterWork" x1="0" y1="0" x2="1" y2="1">
        <stop offset="0" stop-color="#c9cfd6"/>
        <stop offset="0.45" stop-color="#8b929b"/>
        <stop offset="1" stop-color="#5e6670"/>
      </linearGradient>
      <linearGradient id="frostTrees" x1="0" y1="0" x2="0" y2="1">
        <stop offset="0" stop-color="#9aa3c2"/>
        <stop offset="1" stop-color="#dfe3ee"/>
      </linearGradient>
    </defs>
    <path role="img" aria-label="Photo collage of a snow plow truck, a tractor clearing snow and a gloved hand scraping ice"
          d="M0,0 H720 L540,360 C420,390 300,430 200,520 C130,580 60,620 0,640 Z" fill="url(#winterWork)"/>
    <path role="img" aria-label="Photo of snow-covered trees in falling snow"
          d="M720,0 H1200 V380 C1000,330 760,322 540,360 Z" fill="url(#frostTrees)"/>
    <path d="M540,360 C760,322 1000,330 1200,380 V452 C1000,372 760,346 540,362 Z" fill="var(--orange)"/>
    <path d="M380,786 H1200 V924 H380 Z" fill="var(--orange-deep)"/>
    <path d="M0,792 C140,758 420,752 510,806 C550,836 570,880 580,924 H0 Z" fill="var(--charcoal)"/>
  </svg>

  <div class="brand">
    <span class="brand__dot"></span>
    <span class="brand__name">Frostline Lawn &amp; Landscape</span>
  </div>

  <div class="estimate-badge">
    <div class="estimate-badge__inner">
      <span class="estimate-badge__free">FREE</span>
      <span class="estimate-badge__word">Estimates</span>
    </div>
  </div>

  <h1 class="headline">Snow is<br>coming</h1>

  <p class="urgency">Don't Wait Until It's <span class="urgency__accent">TOO LATE</span></p>
  <p class="packages">Seasonal Packages Available</p>

  <section class="services">
    <h2 class="services__title">Services offered</h2>
    <ul class="services__list">
      <li class="services__item">Commercial/Residential</li>
      <li class="services__item">Snow Plowing</li>
      <li class="services__item">Snow Blowing</li>
      <li class="services__item">Snow Shoveling</li>
      <li class="services__item">Ice Removal</li>
      <li class="services__item">Salting/Sanding</li>
    </ul>
  </section>

  <div class="credentials">
    <p class="credentials__license">Fully Licensed and Insured</p>
    <p class="credentials__oncall">Available and ON CALL 24/7</p>
  </div>

  <div class="reserve">
    <p class="reserve__cta">CALL NOW TO RESERVE</p>
    <p class="reserve__phone">XX XXXX XX XXX</p>
  </div>
</main>
</body>
</html>
```